Esthetically Pleasing Core Values and Brand Promise for Accounting Firm

I would like a cohesive design that ties together my core values and brand promise. My firm, Maple Finch Advisory, provides accounting work to small businesses. I prefer modern and clean designs. I want my Core Values and Brand Promise to represent me - sole entrepreneur, married, mother of two kids, modern esthetics, clean lines, organized, colorful (teals, greys, white, yellows)

Industry/Entity Type

Public Accounting

Colors
33b8a4

```html
<!DOCTYPE html>
<html lang="en">
<head>
<meta charset="UTF-8">
<title>Maple Finch Advisory – Brand Promise &amp; Core Values</title>
<link href="https://fonts.googleapis.com/css2?family=Open+Sans:wght@400;600;700;800&display=swap" rel="stylesheet">
<style>
  :root{
    --teal:#33b8a4;
    --teal-deep:#1f9c92;
    --ink:#1e1e1e;
    --text:#333;
    --paper:#f7f7f5;
    --backdrop:#e4e4e2;
    --white:#ffffff;
  }
  *{box-sizing:border-box;margin:0;padding:0}
  html,body{width:1200px;height:900px;overflow:hidden}
  body{background:var(--backdrop);font-family:"Open Sans",Arial,sans-serif;color:var(--text)}
  .flyer{position:absolute;left:290px;top:20px;width:620px;height:860px;background:var(--paper);overflow:hidden;box-shadow:0 4px 18px rgba(0,0,0,.12)}
  .brand-name{position:absolute;left:42px;top:96px;width:240px;color:var(--teal);font-weight:600;font-size:34px;line-height:1.15}
  .hero-photo{position:absolute;left:288px;top:6px;width:310px;height:310px;border-radius:50%;background:radial-gradient(circle at 40% 40%,#9fe7dc,#3cc3b0 55%,#1d8f86)}
  .promise{position:absolute;left:56px;top:258px;font-weight:800;font-size:21px;line-height:1.15;color:var(--ink);text-align:center;width:240px}
  .promise .accent{color:var(--teal)}
  .service{position:absolute;left:40px;width:270px;text-align:center}
  .service-icon{display:block;margin:0 auto 4px}
  .service-tag{display:inline-block;background:var(--teal);color:var(--white);font-size:12px;font-weight:600;letter-spacing:.5px;padding:1px 22px;border-radius:8px}
  .service p{font-size:11px;line-height:1.45;margin-top:6px}
  .service.tax{top:340px}
  .service.accounting{top:488px}
  .team-photo{position:absolute;left:0;top:626px;width:340px;height:234px;background:linear-gradient(90deg,#cfd6dc,#eef1f3 70%,var(--paper))}
  .values-title{position:absolute;left:318px;top:340px;width:302px;height:40px;background:var(--ink);color:var(--white);border-radius:20px 0 0 20px;font-weight:700;font-size:19px;line-height:40px;padding-left:22px;letter-spacing:.5px}
  .values{position:absolute;left:330px;top:398px;width:270px;list-style:none}
  .value{display:flex;gap:14px;align-items:flex-start;height:88px}
  .value-icon{flex:0 0 44px;width:44px;height:44px;border:2px solid var(--teal-deep);border-radius:50%;display:flex;align-items:center;justify-content:center}
  .value h3{font-size:13px;font-weight:600;color:var(--ink);text-transform:uppercase}
  .value p{font-size:10.5px;line-height:1.3;margin-top:2px}
  .footer-band{position:absolute;left:260px;bottom:0;width:360px;height:80px;background:var(--ink);border-top-left-radius:40px 40px}
  .web{position:absolute;right:26px;bottom:50px;color:var(--white);font-size:13px;font-weight:600}
  .call-band{position:absolute;left:0;bottom:0;width:370px;height:44px;background:var(--teal);border-top-right-radius:44px 44px;color:var(--white);font-weight:700;font-size:16px;line-height:44px;padding-left:44px;letter-spacing:.5px}
</style>
</head>
<body>
<main class="flyer">
  <h1 class="brand-name">Maple Finch Advisory</h1>

  <div class="hero-photo" role="img" aria-label="Teal-toned close-up photo of a calculator and financial ledger"></div>

  <h2 class="promise"><span class="accent">BRAND</span> PROMISE<br>Trust, Transparency<br>and <span class="accent">Dependability</span></h2>

  <section class="service tax">
    <svg class="service-icon" width="40" height="44" viewBox="0 0 40 44" fill="none" stroke="#333" stroke-width="2">
      <rect x="6" y="2" width="28" height="40" rx="2"/>
      <line x1="11" y1="10" x2="29" y2="10"/><line x1="11" y1="18" x2="29" y2="18"/>
      <line x1="11" y1="24" x2="29" y2="24"/><line x1="11" y1="30" x2="22" y2="30"/>
    </svg>
    <span class="service-tag">TAX</span>
    <p>Maple Finch provides all clients with a trusted tax advisor who provides accuracy in all filings and ensures your compliance with all government agencies.</p>
  </section>

  <section class="service accounting">
    <svg class="service-icon" width="44" height="44" viewBox="0 0 44 44" fill="none" stroke="#333" stroke-width="2">
      <rect x="3" y="6" width="22" height="32" rx="2"/>
      <rect x="20" y="14" width="20" height="26" rx="2" fill="#f7f7f5"/>
      <rect x="24" y="18" width="12" height="5"/>
      <circle cx="26" cy="29" r="1" fill="#333"/><circle cx="30" cy="29" r="1" fill="#333"/><circle cx="34" cy="29" r="1" fill="#333"/>
      <circle cx="26" cy="35" r="1" fill="#333"/><circle cx="30" cy="35" r="1" fill="#333"/><circle cx="34" cy="35" r="1" fill="#333"/>
    </svg>
    <span class="service-tag">ACCOUNTING</span>
    <p>Maple Finch provides all business owners with the financial visibility needed to foster growth and facilitate goals.</p>
  </section>

  <div class="team-photo" role="img" aria-label="Photo of a smiling businesswoman in front of colleagues at a meeting table"></div>

  <h2 class="values-title">OUR CORE VALUES</h2>
  <ul class="values">
    <li class="value">
      <span class="value-icon"><svg width="22" height="26" viewBox="0 0 22 26" fill="none" stroke="#333" stroke-width="1.8"><circle cx="11" cy="5" r="3.5"/><path d="M6 25V12h10v13M11 18v7"/></svg></span>
      <div><h3>Empower</h3><p>we are dedicated, appreciative and respectful of people's time</p></div>
    </li>
    <li class="value">
      <span class="value-icon"><svg width="26" height="26" viewBox="0 0 26 26" fill="none" stroke="#333" stroke-width="1.8"><circle cx="11" cy="11" r="7"/><line x1="16" y1="16" x2="23" y2="23"/><circle cx="11" cy="9" r="2"/><path d="M7 15c1-3 7-3 8 0"/></svg></span>
      <div><h3>Client Focused</h3><p>we provide a personal service that goes above the standards of professional care.</p></div>
    </li>
    <li class="value">
      <span class="value-icon"><svg width="26" height="24" viewBox="0 0 26 24" fill="none" stroke="#333" stroke-width="1.6"><line x1="13" y1="2" x2="13" y2="21"/><line x1="4" y1="5" x2="22" y2="5"/><line x1="8" y1="22" x2="18" y2="22"/><path d="M4 5l-3 8h6zM22 5l-3 8h6z"/></svg></span>
      <div><h3>Rectitude</h3><p>we know the difference between what we have the right to do and what the right thing to do is.</p></div>
    </li>
    <li class="value">
      <span class="value-icon"><svg width="18" height="26" viewBox="0 0 18 26" fill="none" stroke="#333" stroke-width="1.8" stroke-linejoin="round"><path d="M11 1L3 14h6l-2 11 8-14H9z"/></svg></span>
      <div><h3>Relentless</h3><p>we believe that the longer we try to do our best, the better we become.</p></div>
    </li>
  </ul>

  <div class="footer-band"></div>
  <p class="web">www.maplefinchadvisory.com</p>
  <p class="call-band">CALL US TODAY-555.014.2290</p>
</main>
</body>
</html>
```